HML5 Web Application Design

We need a graphic design to give a HTML web application a modern look and feel. The design should be clean and neat with a metro inspired interface. All application uses vormanta controls so any experience with these would be great.
Perhaps you could also include a few screenshots of your previous work

Industry/Entity Type

Graphic Design

Requirements
Must have
• Must be HTML 5 compliant

```html
<!DOCTYPE html>
<html lang="en">
<head>
<meta charset="utf-8">
<title>Supplier Transactions Screen</title>
<link href="https://fonts.googleapis.com/css2?family=Roboto+Condensed:wght@700&family=Arimo:wght@400;700&display=swap" rel="stylesheet">
<style>
:root{
  --header-top:#455f7c;
  --header-bottom:#2f4661;
  --nav-bg:#22354a;
  --nav-line:#10202f;
  --page-bg:#efefef;
  --panel-bg:#ffffff;
  --border:#d4d4d4;
  --row-line:#e2e2e2;
  --head-bg:#f3f3f3;
  --title:#243a52;
  --text:#555555;
  --label:#6b6b6b;
  --link:#f29a1e;
  --page-link:#8b1a1a;
  --footer-bg:#ffffff;
}
*{box-sizing:border-box;margin:0;padding:0}
html,body{width:1200px;height:706px;overflow:hidden}
body{position:relative;background:var(--page-bg);font-family:"Arimo",Arial,sans-serif;color:var(--text)}
.site-header{position:absolute;left:0;top:0;width:1200px;height:60px;background:linear-gradient(var(--header-top),var(--header-bottom))}
.brand{position:absolute;left:23px;top:14px;font-family:"Roboto Condensed",sans-serif;font-weight:700;font-size:31px;color:#fff;letter-spacing:-.3px}
.welcome{position:absolute;right:22px;top:23px;font-size:14px;font-weight:700;color:#eef2f6}
.welcome a{color:var(--link);font-weight:400;font-size:13px;text-decoration:underline}
.main-nav{position:absolute;left:0;top:60px;width:1200px;height:42px;background:var(--nav-bg);border-top:1px solid var(--nav-line)}
.main-nav ul{list-style:none;position:absolute;right:0;top:0;display:flex;height:42px;align-items:center}
.main-nav li{font-size:12.5px;font-weight:700;color:#fff;letter-spacing:.3px;margin-left:43px;display:flex;align-items:center;gap:6px}
.main-nav li:last-child{margin-right:19px}
.page-title{position:absolute;left:19px;top:122px;font-family:"Roboto Condensed",sans-serif;font-weight:700;font-size:26px;color:var(--title);letter-spacing:-.2px}
.date-field{position:absolute;top:128px;display:flex;align-items:center;gap:7px}
.date-field label{font-family:"Roboto Condensed",sans-serif;font-weight:700;font-size:15px;color:var(--label)}
.date-input{display:flex;width:134px;height:23px;border:1px solid #c9c9c9;background:#fff}
.date-input span{flex:1;font-size:13.5px;color:#555;padding:3px 6px}
.date-input i{width:26px;border-left:1px solid #c9c9c9;background:#f2f2f2;display:flex;align-items:center;justify-content:center}
.from{left:714px}
.to{left:985px}
.transactions{position:absolute;left:19px;top:161px;width:1161px;height:486px;background:var(--panel-bg);border:1px solid var(--border);border-radius:3px}
table{border-collapse:collapse;width:100%;font-size:13.5px}
th{height:34px;background:var(--head-bg);text-align:left;font-family:"Roboto Condensed",sans-serif;font-weight:700;font-size:15px;color:var(--label);padding:0 14px;border-right:1px solid var(--row-line);border-bottom:1px solid var(--row-line);position:relative}
th svg{position:absolute;right:12px;top:12px}
td{height:39.7px;padding:0 14px;border-right:1px solid var(--row-line);border-bottom:1px solid var(--row-line)}
th:last-child,td:last-child{border-right:none}
.col-date{width:195px}.col-type{width:225px}.col-ref{width:242px}.col-amt{width:258px}
.table-info{position:absolute;left:15px;top:453px;font-size:13.5px}
.pager{position:absolute;right:13px;top:443px;display:flex;height:31px;border:1px solid #cfcfcf;border-radius:3px;overflow:hidden;font-size:12.5px}
.pager span{display:flex;align-items:center;padding:0 14px;border-left:1px solid #cfcfcf;background:#f3f3f3;color:var(--page-link)}
.pager span:first-child{border-left:none;color:#999;padding:0 15px}
.pager .current{background:#fff;color:#999}
.site-footer{position:absolute;left:0;top:656px;width:1200px;height:50px;background:var(--footer-bg);border-top:1px solid #ddd;text-align:center;font-size:12px;color:#333;padding-top:18px;letter-spacing:.2px}
</style>
</head>
<body>
<header class="site-header">
  <div class="brand">Your logo here</div>
  <div class="welcome">Welcome, Superuser! <a href="#">Log off</a></div>
</header>
<nav class="main-nav">
  <ul>
    <li><svg width="11" height="10" viewBox="0 0 11 10"><path d="M5.5 0L0 5h1.5v5h3V7h2v3h3V5H11z" fill="#fff"/></svg>Home</li>
    <li>Pin Request</li>
    <li>Transactions</li>
    <li>Tax Details</li>
    <li>Users</li>
    <li>Suppliers</li>
    <li>Queries</li>
    <li>LA Staff Queries</li>
  </ul>
</nav>
<h1 class="page-title">Supplier Transactions Screen</h1>
<div class="date-field from"><label>Date From:</label><div class="date-input"><span>01/01/2013</span><i><svg width="13" height="12" viewBox="0 0 13 12"><rect x=".5" y=".5" width="12" height="11" fill="#fff" stroke="#999"/><rect x="1" y="1" width="11" height="3" fill="#d8473b"/><path d="M3 6h2M6 6h2M9 6h2M3 8.5h2M6 8.5h2M9 8.5h2" stroke="#b55" stroke-width="1.2"/></svg></i></div></div>
<div class="date-field to"><label>Date to:</label><div class="date-input"><span>02/08/2013</span><i><svg width="13" height="12" viewBox="0 0 13 12"><rect x=".5" y=".5" width="12" height="11" fill="#fff" stroke="#999"/><rect x="1" y="1" width="11" height="3" fill="#d8473b"/><path d="M3 6h2M6 6h2M9 6h2M3 8.5h2M6 8.5h2M9 8.5h2" stroke="#b55" stroke-width="1.2"/></svg></i></div></div>
<section class="transactions">
  <table>
    <thead><tr>
      <th class="col-date">Date<svg width="10" height="10" viewBox="0 0 10 10"><path d="M2 4l3-3 3 3M2 6l3 3 3-3" fill="none" stroke="#999" stroke-width="1.2"/></svg></th>
      <th class="col-type">Type<svg width="10" height="10" viewBox="0 0 10 10"><path d="M2 4l3-3 3 3M2 6l3 3 3-3" fill="none" stroke="#999" stroke-width="1.2"/></svg></th>
      <th class="col-ref">Reference<svg width="10" height="10" viewBox="0 0 10 10"><path d="M2 4l3-3 3 3M2 6l3 3 3-3" fill="none" stroke="#999" stroke-width="1.2"/></svg></th>
      <th class="col-amt">Amount<svg width="10" height="10" viewBox="0 0 10 10"><path d="M2 4l3-3 3 3M2 6l3 3 3-3" fill="none" stroke="#999" stroke-width="1.2"/></svg></th>
      <th>Status<svg width="10" height="10" viewBox="0 0 10 10"><path d="M2 4l3-3 3 3M2 6l3 3 3-3" fill="none" stroke="#999" stroke-width="1.2"/></svg></th>
    </tr></thead>
    <tbody>
      <tr><td>21/01/2013</td><td>Inv</td><td>12345</td><td>100</td><td>Received</td></tr>
      <tr><td>16/02/2012</td><td>Payment</td><td>456456</td><td>80</td><td>Payment</td></tr>
      <tr><td>24/03/2012</td><td>Inv</td><td>324567</td><td>20</td><td>Received</td></tr>
      <tr><td>19/04/2010</td><td>Payment</td><td>546543</td><td>150</td><td>Payment</td></tr>
      <tr><td>01/05/2010</td><td>Inv</td><td>125432</td><td>30</td><td>Received</td></tr>
      <tr><td>03/06/2009</td><td>Payment</td><td>851413</td><td>40</td><td>Payment</td></tr>
      <tr><td>09/07/2008</td><td>Inv</td><td>585210</td><td>90</td><td>Received</td></tr>
      <tr><td>15/08/2008</td><td>Payment</td><td>112947</td><td>100</td><td>Payment</td></tr>
      <tr><td>11/09/2007</td><td>Inv</td><td>048211</td><td>110</td><td>Received</td></tr>
      <tr><td>26/10/2000</td><td>Payment</td><td>235432</td><td>200</td><td>Payment</td></tr>
    </tbody>
  </table>
  <div class="table-info">Showing 1 to 10 of 50 entries</div>
  <div class="pager"><span>&larr; Previous</span><span class="current">1</span><span>2</span><span>3</span><span>4</span><span>5</span><span>Next &rarr;</span></div>
</section>
<footer class="site-footer">Copyright 2013 - KVT. All Rights Reserved.</footer>
</body>
</html>
```